Pipeline management & construction company needs nice brochure

Red Mesa Engineering & Construction, LLC (www.redmesaec.example) is a company focused on the midstream oil and gas / pipeline business. We plan, route, design, manage, and construction pipelines and related facilities. We need a brochure to summarize our services as well as give a brief listing of projects completed/desired.

Industry/Entity Type

Construction

Font styles to use
Serif

```html
<!DOCTYPE html>
<html lang="en">
<head>
<meta charset="utf-8">
<title>Red Mesa Engineering &amp; Construction — Brochure Spread</title>
<link href="https://fonts.googleapis.com/css2?family=Ubuntu:ital,wght@0,400;0,500;0,700;1,500;1,700&display=swap" rel="stylesheet">
<style>
  :root{
    --backdrop:#d8d8d8;
    --page:#e2b90b;
    --page-deep:#c9a200;
    --page-light:#ecc935;
    --ink:#2b2406;
    --ink-soft:#4a3e08;
    --ink-head:#1f1a03;
    --tab:#1c1c1c;
  }
  *{box-sizing:border-box;margin:0;padding:0}
  html,body{width:1200px;height:902px;overflow:hidden;background:var(--backdrop)}
  body{font-family:"Ubuntu",sans-serif;color:var(--ink);position:relative}
  .spread{position:absolute;left:170px;top:120px;width:860px;height:640px;display:flex;box-shadow:0 14px 34px rgba(0,0,0,.22)}
  .page{position:relative;width:430px;height:640px;background:var(--page);overflow:hidden}
  .page--left{box-shadow:inset -18px 0 24px -14px rgba(0,0,0,.25)}
  .page--right{box-shadow:inset 18px 0 24px -14px rgba(0,0,0,.22)}
  .landscape{position:absolute;left:0;right:0;bottom:0;height:70%;
    background:linear-gradient(180deg,rgba(226,185,11,0) 0%,rgba(180,140,0,.35) 45%,rgba(150,115,0,.45) 100%)}
  .portrait{position:absolute;left:28px;top:20px;width:120px;height:250px;
    background:linear-gradient(180deg,#d9b800 0 12%,#2a2a2a 12% 100%);border-radius:50px 50px 4px 4px;opacity:.9}
  .profile{position:absolute;left:158px;top:22px;width:250px}
  .name{font-weight:700;font-size:20px;color:var(--ink-head);letter-spacing:.2px}
  .contact{font-size:8.5px;line-height:1.3;font-weight:500;margin-top:2px}
  .contact b{font-weight:700}
  .label{font-weight:700;font-size:9px;text-transform:uppercase;margin-top:8px;color:var(--ink-head)}
  .body{font-size:7.8px;line-height:1.32;color:var(--ink-soft)}
  .edu{display:flex;gap:12px;margin-top:8px;font-size:7.8px;line-height:1.32}
  .edu .label{margin-top:0}
  .left-copy{position:absolute;left:28px;right:26px;top:300px}
  .left-copy p{margin-bottom:10px}
  .job{margin-bottom:9px}
  .job-firm{font-weight:700;font-size:8.2px;color:var(--ink-head)}
  .job-firm::before{content:"• "}
  .job-title{font-weight:700;font-style:italic;font-size:8px;color:var(--ink-head);margin-left:8px}
  .job .body{margin-left:8px}
  .right-copy{position:absolute;left:30px;right:30px;top:26px}
  .folio{position:absolute;bottom:16px;width:24px;height:14px;border-radius:7px;background:var(--tab);color:var(--page-light);font-size:8px;font-weight:700;display:flex;align-items:center;justify-content:center}
  .folio--left{left:22px}
  .folio--right{right:22px}
</style>
</head>
<body>
  <main class="spread">
    <section class="page page--left">
      <div class="landscape" role="img" aria-label="Faded photo of a pipeline right-of-way across grassland"></div>
      <div class="portrait" role="img" aria-label="Photo of the company president in a suit and hard hat"></div>
      <div class="profile">
        <h1 class="name">Dale Harmon</h1>
        <div class="contact">
          <b>4810 Caliche Road, Ste B</b><br>
          <b>Alvarado Springs, TX 78000</b><br>
          Email: <b>dharmon@redmesaec.example</b><br>
          Contact Person: <b>555.014.2290</b>
        </div>
        <h2 class="label">Experience Summary</h2>
        <p class="body">A project oriented individual with international, as well as domestic experience. More than fifteen years experience in onshore pipeline construction. Strong industry knowledge of design, analysis, and operation of pipelines and related facilities. Experience in Horizontal Directional Drilling operations and design and with compliance and implementation of DOT Safety Regulations 49 CFR Part 192 and Part 195 as well as ASME/ANSI B31.4 and B31.8.</p>
        <div class="edu">
          <h2 class="label">Education<br><span class="body" style="font-weight:400">1997-2001</span></h2>
          <p>Gulf Plains State University, Harlow, Texas. Bachelor of Science, Mechanical Engineering Technology, December 2001</p>
        </div>
        <h2 class="label">Experience</h2>
        <div class="job" style="margin-top:3px">
          <div class="job-firm">Red Mesa Engineering &amp; Construction, LLC, Alvarado Springs, Texas</div>
          <div class="job-title">PRESIDENT – December 2012 to Present</div>
        </div>
      </div>
      <div class="left-copy body">
        <p>A project oriented individual with international, as well as domestic experience. More than fifteen years experience in onshore pipeline construction. Strong industry knowledge of design, analysis, and operation of pipelines and related facilities. Experience in Horizontal Directional Drilling operations and design and with compliance and implementation of DOT Safety Regulations 49 CFR Part 192 and Part 195 as well as ASME/ANSI B31.4 and B31.8.</p>
        <p>A project oriented individual with international, as well as domestic experience. More than fifteen years experience in onshore pipeline construction. Strong industry knowledge of design, analysis, and operation of pipelines and related facilities. Experience in Horizontal Directional Drilling operations and design and with compliance and implementation of DOT Safety Regulations 49 CFR Part 192 and Part 195 as well as ASME/ANSI B31.4 and B31.8.</p>
        <p>A project oriented individual with international, as well as domestic experience. More than fifteen years experience in onshore pipeline construction. Strong industry knowledge of design, analysis, and operation of pipelines and related facilities. Experience in Horizontal Directional Drilling operations and design and with compliance and implementation of DOT Safety Regulations 49 CFR Part 192 and Part 195 as well as ASME/ANSI B31.4 and B31.8.</p>
        <p>A project oriented individual with international, as well as domestic experience. More than fifteen years experience in onshore pipeline construction. Strong industry knowledge of design, analysis, and operation of pipelines and related facilities. Experience in Horizontal Directional Drilling operations and design and with compliance and implementation of DOT Safety Regulations 49 CFR Part 192 and Part 195 as well as ASME/ANSI B31.4 and B31.8.</p>
      </div>
      <div class="folio folio--left">6</div>
    </section>

    <section class="page page--right">
      <div class="landscape" role="img" aria-label="Faded photo of a pipeline right-of-way across grassland"></div>
      <div class="right-copy">
        <div class="job"><div class="job-firm">Red Mesa Engineering &amp; Construction, LLC, Alvarado Springs, Texas</div><div class="job-title">PRESIDENT – December 2012 to Present</div><p class="body">A project oriented individual with international, as well as domestic experience. More than fifteen years experience in onshore pipeline construction.</p></div>
        <div class="job"><div class="job-firm">Red Mesa Engineering &amp; Construction, LLC, Alvarado Springs, Texas</div><div class="job-title">PRESIDENT – December 2012 to Present</div><p class="body">A project oriented individual with international, as well as domestic experience. More than fifteen years experience in onshore pipeline construction.</p></div>
        <div class="job"><div class="job-firm">Red Mesa Engineering &amp; Construction, LLC, Alvarado Springs, Texas</div><div class="job-title">PRESIDENT – December 2012 to Present</div><p class="body">A project oriented individual with international, as well as domestic experience. More than fifteen years experience in onshore pipeline construction. A project oriented individual with international, as well as domestic experience. More than fifteen years experience in onshore pipeline construction.</p></div>
        <div class="job"><div class="job-firm">Red Mesa Engineering &amp; Construction, LLC, Alvarado Springs, Texas</div><div class="job-title">PRESIDENT – December 2012 to Present</div><p class="body">A project oriented individual with international, as well as domestic experience. More than fifteen years experience in onshore pipeline construction. A project oriented individual with international, as well as domestic experience. More than fifteen years experience in onshore pipeline construction.</p></div>
        <div class="job"><div class="job-firm">Red Mesa Engineering &amp; Construction, LLC, Alvarado Springs, Texas</div><div class="job-title">PRESIDENT – December 2012 to Present</div><p class="body">A project oriented individual with international, as well as domestic experience. More than fifteen years experience in onshore pipeline construction. A project oriented individual with international, as well as domestic experience. More than fifteen years experience in onshore pipeline construction.</p></div>
        <div class="job"><div class="job-firm">Red Mesa Engineering &amp; Construction, LLC, Alvarado Springs, Texas</div><div class="job-title">PRESIDENT – December 2012 to Present</div><p class="body">A project oriented individual with international, as well as domestic experience. More than fifteen years experience in onshore pipeline construction. A project oriented individual with international, as well as domestic experience. More than fifteen years experience in onshore pipeline construction.</p></div>
        <div class="job"><div class="job-firm">Red Mesa Engineering &amp; Construction, LLC, Alvarado Springs, Texas</div><div class="job-title">PRESIDENT – December 2012 to Present</div><p class="body">A project oriented individual with international, as well as domestic experience. More than fifteen years experience in onshore pipeline construction. A project oriented individual with international, as well as domestic experience. More than fifteen years experience in onshore pipeline construction.</p></div>
        <div class="job"><div class="job-firm">Red Mesa Engineering &amp; Construction, LLC, Alvarado Springs, Texas</div><div class="job-title">PRESIDENT – December 2012 to Present</div><p class="body">A project oriented individual with international, as well as domestic experience. More than fifteen years experience in onshore pipeline construction. A project oriented individual with international, as well as domestic experience. More than fifteen years experience in onshore pipeline construction.</p></div>
      </div>
      <div class="folio folio--right">7</div>
    </section>
  </main>
</body>
</html>
```